Sonoma County Winery needs a fresh label design for new line of natural wines

The growing natural wine market requires a fresh perspective. Traditional wine labels don't attract the attention of natural wine buyers or the spirit for which they were made. Natural wines tend to be sustainable, organic and biodynamic. Natural wines also break norms and have disrupted the commercial wine industry with their non-traditional imagery and label designs. Natural wines stick out on the shelf for their brighter colors, illustrations and more handwritten font selections. Bottles are typically flint (clear glass) showing the true color of the wine, red and white. Red wines are typically not opaque, but rather light colored with zero filtration (
see attached pic). No capsule is used, therefore, the cork is shown through the glass bottle.

Target Market(s)

Wine buyers between the ages of 21-35 generally living in large cities, but more specifically San Francisco and Los Angeles

Requirements
Must have
• Dimensions:2 3/4 Inches Wide5 1/4 Inches TallIntended to print on Bright White Felt paper CMYK
Nice to have
• It may not have any words on the front label at all. It's more about symbolism and color and design then it is about the actual brand name (which will go on the back where all the legal stuff is). I've included several bottle shots from natural winemakers that may give you a sense that there is no one way to design a natural wine label, but rather several directions at this early stage in the market cycle
Should not have
• If it looks and smells like a traditional wine label, it's probably not the right idea

```html
<!DOCTYPE html>
<html lang="en">
<head>
<meta charset="UTF-8">
<title>Natural Wine Label</title>
<link rel="stylesheet" href="https://fonts.googleapis.com/css2?family=Amatic+SC:wght@700&family=Patrick+Hand&display=swap">
<style>
  :root {
    --backdrop: #f3f3f3;
    --sky-top: #f7568f;
    --sky-mid: #ff7f7a;
    --sky-low: #ffb07a;
    --hills-light: #b0508f;
    --hills-mid: #7a3b7e;
    --hills-deep: #3c2c52;
    --ink-title: #392c5c;
    --ink-light: #ffffff;
  }
  * { margin: 0; padding: 0; box-sizing: border-box; }
  html, body {
    width: 960px;
    height: 1200px;
    overflow: hidden;
    background: var(--backdrop);
  }
  .canvas {
    position: relative;
    width: 960px;
    height: 1200px;
  }
  .label {
    position: absolute;
    left: 210px;
    top: 50px;
    width: 540px;
    height: 1100px;
    overflow: hidden;
    background: linear-gradient(180deg, var(--sky-top) 0%, var(--sky-mid) 32%, var(--sky-low) 52%);
  }
  .label__title {
    position: absolute;
    top: 178px;
    left: 0;
    width: 100%;
    text-align: center;
    font-family: "Amatic SC", cursive;
    font-weight: 700;
    font-size: 132px;
    line-height: 1;
    letter-spacing: 4px;
    color: var(--ink-title);
  }
  .label__tagline {
    position: absolute;
    top: 322px;
    left: 0;
    width: 100%;
    text-align: center;
    font-family: "Patrick Hand", cursive;
    font-size: 40px;
    line-height: 1;
    color: var(--ink-light);
  }
  .label__landscape {
    position: absolute;
    left: 0;
    top: 560px;
    width: 100%;
    height: 540px;
  }
  .label__volume {
    position: absolute;
    top: 1010px;
    left: 0;
    width: 100%;
    text-align: center;
    font-family: "Amatic SC", cursive;
    font-weight: 700;
    font-size: 76px;
    line-height: 1;
    color: var(--ink-light);
  }
</style>
</head>
<body>
  <main class="canvas">
    <section class="label">
      <h1 class="label__title">LOREM IPSUM</h1>
      <p class="label__tagline">Contrary to popular belief</p>
      <svg class="label__landscape" role="img" aria-label="Illustration of layered purple mountains at sunset reflected in a still lake" viewBox="0 0 540 540" preserveAspectRatio="none">
        <defs>
          <linearGradient id="landscape-tone" x1="0" y1="0" x2="0" y2="1">
            <stop offset="0" stop-color="var(--hills-light)" stop-opacity="0"/>
            <stop offset="0.12" stop-color="var(--hills-light)"/>
            <stop offset="0.5" stop-color="var(--hills-mid)"/>
            <stop offset="1" stop-color="var(--hills-deep)"/>
          </linearGradient>
        </defs>
        <rect x="0" y="0" width="540" height="540" fill="url(#landscape-tone)"/>
      </svg>
      <p class="label__volume">1l</p>
    </section>
  </main>
</body>
</html>
```